Fun and Splashy Flyer Design

We need a flyer designed for our new car cleaning brand! We have looked around, and the stock options either look way too dark/serious/exclusive, or they look too shiny/stock image.

We need something that can be more subtle, that works with our work van.

For this project we would like a photoshop file with individual layers, and you can just put placeholder text for the main slogan, a header 1, header 2, bullet point and body text.

What we're really looking for are the transitions between images and elements, font colours and pairings and design accents.

We want the brand to be fun, clean, happy and straightforward (slightly minimalist). Please message if you have any questions!

```html
<!DOCTYPE html>
<html lang="en">
<head>
<meta charset="utf-8">
<title>Brightway Mobile – Flyer</title>
<link href="https://fonts.googleapis.com/css2?family=Barlow:wght@400;600;700;800&family=Open+Sans:wght@400;600&display=swap" rel="stylesheet">
<style>
:root{
  --blue:#1c5aa8;
  --blue-dark:#123f7e;
  --blue-light:#2b78c9;
  --yellow:#ffe21a;
  --yellow-deep:#f5c400;
  --ink:#4a4f57;
  --white:#ffffff;
  --bubble:#cfe6fa;
}
*{margin:0;padding:0;box-sizing:border-box}
html,body{width:900px;height:1200px;overflow:hidden;background:var(--white)}
.flyer{position:relative;width:900px;height:1200px;background:var(--white);font-family:"Open Sans",Arial,sans-serif;color:var(--ink)}
.brand{position:absolute;left:30px;top:30px;width:180px;height:170px;display:flex;flex-direction:column;align-items:center;justify-content:center;gap:10px}
.brand-dot{width:84px;height:84px;border-radius:50%;background:var(--yellow)}
.brand-name{font-family:"Barlow",Arial,sans-serif;font-weight:800;font-size:24px;line-height:1.05;color:var(--blue);text-align:center;text-transform:uppercase}
.headline-band{position:absolute;left:228px;top:30px;width:642px;height:124px;background:var(--blue);display:flex;align-items:center;justify-content:center;padding:0 24px}
.headline{font-family:"Barlow",Arial,sans-serif;font-weight:700;font-size:44px;line-height:1.1;color:var(--white);text-align:center}
.tagline-band{position:absolute;left:228px;top:162px;width:642px;height:40px;background:var(--yellow);display:flex;align-items:center;justify-content:center}
.tagline{font-family:"Barlow",Arial,sans-serif;font-weight:700;font-size:22px;color:var(--blue-dark)}
.intro{position:absolute;left:40px;top:240px;width:355px;font-size:13.5px;line-height:1.55}
.bubbles{position:absolute;left:40px;top:440px;width:350px;height:150px;border-radius:12px;background:radial-gradient(circle at 40% 50%,var(--bubble),#eef6fd 70%,var(--white))}
.section-title{position:absolute;left:40px;top:612px;font-family:"Barlow",Arial,sans-serif;font-weight:700;font-size:24px;color:var(--blue-dark)}
.section-body{position:absolute;left:40px;top:648px;width:355px;font-size:13.5px;line-height:1.55}
.van{position:absolute;left:30px;top:820px;width:370px;height:170px;border-radius:40px 60px 14px 14px;background:linear-gradient(180deg,#f4f7fb,#dfe8f2)}
.price-panel{position:absolute;left:420px;width:455px;background:linear-gradient(180deg,var(--blue-light),var(--blue-dark));padding:46px 20px 20px}
.panel-one{top:250px;height:410px}
.panel-two{top:690px;height:400px}
.panel-tab{position:absolute;left:50%;top:-14px;transform:translateX(-50%);width:250px;height:38px;background:var(--yellow);border-radius:4px;display:flex;align-items:center;justify-content:center;font-family:"Barlow",Arial,sans-serif;font-weight:700;font-size:20px;color:var(--blue-dark)}
.price-list{list-style:none;display:flex;flex-direction:column;gap:12px}
.price-row{display:flex;align-items:center;height:46px;border-bottom:1px solid rgba(255,255,255,.25);padding-bottom:10px}
.row-label{width:118px;height:36px;background:var(--yellow);display:flex;align-items:center;padding-left:10px;font-family:"Barlow",Arial,sans-serif;font-weight:600;font-size:16px;color:var(--blue-dark);margin-right:14px}
.row-text{flex:1;font-size:11.5px;line-height:1.35;color:var(--white)}
.row-price{font-family:"Barlow",Arial,sans-serif;font-weight:700;font-size:22px;color:var(--yellow)}
.contact-bar{position:absolute;left:0;bottom:0;width:900px;height:92px;background:var(--blue);display:flex;align-items:center;justify-content:center;gap:34px;font-family:"Barlow",Arial,sans-serif;font-weight:700;font-size:30px;color:var(--white)}
.contact-divider{width:3px;height:40px;background:var(--yellow)}
.contact-item{display:flex;align-items:center;gap:12px}
</style>
</head>
<body>
<main class="flyer">
  <div class="brand">
    <span class="brand-dot"></span>
    <span class="brand-name">Brightway<br>Mobile</span>
  </div>

  <header class="headline-band">
    <h1 class="headline">The Easiest Route to a Sparkling, Clean Car!</h1>
  </header>
  <div class="tagline-band"><p class="tagline">Lorem ipsum dolor sit amet, consectetuer</p></div>

  <p class="intro">Brightway Car Cleaning is the latest exciting addition to the Brightway Group of Companies. We felt that there was a gap in the market between a DIY coin operated car wash, and an expensive, high end detailing. After months on the drawing board, we've created an awesome new service using high-end equipment and a refined process to leave your car sparkling clean... without a massive detailing bill.</p>

  <div class="bubbles" role="img" aria-label="Cluster of light blue soap bubbles"></div>

  <h2 class="section-title">LOREM IPSUM</h2>
  <p class="section-body">Lorem ipsum dolor sit amet, consectetuer adipiscing elit, sed diam nonummy nibh euismod tincidunt ut laoreet dolore magna aliquam erat volutpat. Ut wisi enim ad minim veniam, quis nostrud exerci tation ullamcorper suscipit lobortis nisl ut aliquip ex ea commodo consequat.</p>

  <div class="van" role="img" aria-label="White branded work van with blue and yellow livery"></div>

  <section class="price-panel panel-one">
    <div class="panel-tab">LOREM IPSUM</div>
    <ul class="price-list">
      <li class="price-row"><span class="row-label">Lorem ipsum</span><span class="row-text">Lorem ipsum dolor sit amet, consectetuer adipiscing elit, sed</span><span class="row-price">$00.00</span></li>
      <li class="price-row"><span class="row-label">Lorem ipsum</span><span class="row-text">Lorem ipsum dolor sit amet, consectetuer adipiscing elit, sed</span><span class="row-price">$00.00</span></li>
      <li class="price-row"><span class="row-label">Lorem ipsum</span><span class="row-text">Lorem ipsum dolor sit amet, consectetuer adipiscing elit, sed</span><span class="row-price">$00.00</span></li>
      <li class="price-row"><span class="row-label">Lorem ipsum</span><span class="row-text">Lorem ipsum dolor sit amet, consectetuer adipiscing elit, sed</span><span class="row-price">$00.00</span></li>
      <li class="price-row"><span class="row-label">Lorem ipsum</span><span class="row-text">Lorem ipsum dolor sit amet, consectetuer adipiscing elit, sed</span><span class="row-price">$00.00</span></li>
      <li class="price-row"><span class="row-label">Lorem ipsum</span><span class="row-text">Lorem ipsum dolor sit amet, consectetuer adipiscing elit, sed</span><span class="row-price">$00.00</span></li>
    </ul>
  </section>

  <section class="price-panel panel-two">
    <div class="panel-tab">LOREM IPSUM</div>
    <ul class="price-list">
      <li class="price-row"><span class="row-label">Lorem ipsum</span><span class="row-text">Lorem ipsum dolor sit amet, consectetuer adipiscing elit, sed</span><span class="row-price">$00.00</span></li>
      <li class="price-row"><span class="row-label">Lorem ipsum</span><span class="row-text">Lorem ipsum dolor sit amet, consectetuer adipiscing elit, sed</span><span class="row-price">$00.00</span></li>
      <li class="price-row"><span class="row-label">Lorem ipsum</span><span class="row-text">Lorem ipsum dolor sit amet, consectetuer adipiscing elit, sed</span><span class="row-price">$00.00</span></li>
      <li class="price-row"><span class="row-label">Lorem ipsum</span><span class="row-text">Lorem ipsum dolor sit amet, consectetuer adipiscing elit, sed</span><span class="row-price">$00.00</span></li>
      <li class="price-row"><span class="row-label">Lorem ipsum</span><span class="row-text">Lorem ipsum dolor sit amet, consectetuer adipiscing elit, sed</span><span class="row-price">$00.00</span></li>
      <li class="price-row"><span class="row-label">Lorem ipsum</span><span class="row-text">Lorem ipsum dolor sit amet, consectetuer adipiscing elit, sed</span><span class="row-price">$00.00</span></li>
    </ul>
  </section>

  <footer class="contact-bar">
    <span class="contact-item">(+555) 014 229 000</span>
    <span class="contact-divider"></span>
    <span class="contact-item">www.brightwaydetail.ca</span>
  </footer>
</main>
</body>
</html>
```